The Driftwood Caster----- Wade Pellman----- Kellow Creek Bronzeback ------www.thedriftwoodcaster.test-----

Hello Fishermen,
The Umpqua rivers peaceful beauty is like no other river, the private Hollis section offers trophy bass fishing along with 100 fish days. Spin cast or fly fish for bass. This 8 hour fishing trip takes you into a remote section of ranches and wilderness abundant with not only thousands of bass per mile...... but wildlife and scenery are breath taking in this quite section of river.
This trip is for everyone, easy for the Grand Parents and the grand kids...... Women love this trip with the warm weather and easy fishing.
So Let's go Fishing...... please call or email us today and book your trip or with any questions you have.
Vacation Rentals, Motels and R.V parks all available close by.

Email us at: driftwoodcaster@mailbrook.test
Visit our website at: www.thedriftwoodcaster.test
Call us at: 541-555-0148

Thank you for fishing with us,
Wade Pellman

return address;
Wade Pellman
p.o. box 712
Elkton, Oregon 97521

****NOTE for front of post card layout person should go to our website home page for ideas, and photos. Please feel free to change our message above to correct grammar and make read smoother, Thank you.....

there is no contest....not sure how that got there...

```html
<!DOCTYPE html>
<html lang="en">
<head>
<meta charset="utf-8">
<title>The Driftwood Caster – Postcard</title>
<link rel="stylesheet" href="https://fonts.googleapis.com/css2?family=Oswald:wght@500;600;700&family=Sansita:wght@700&family=Arimo:ital,wght@0,400;1,700&display=swap">
<style>
  :root {
    --page: #ffffff;
    --sunset-top: #ec8a34;
    --sunset-bottom: #c2400f;
    --panel: rgba(70, 40, 20, 0.55);
    --cream: #fff6ea;
    --sage: #b9d48c;
    --back-bg: #eef0f8;
    --photo-top: #6f8f62;
    --photo-bottom: #4f7441;
    --ink: #2e2e33;
    --teal: #27a2b7;
    --rule: #c3c6d2;
  }
  * { box-sizing: border-box; margin: 0; padding: 0; }
  html, body { width: 779px; height: 1200px; overflow: hidden; background: var(--page); }
  body { position: relative; }

  .card { position: absolute; overflow: hidden; }

  /* Front */
  .card--front { left: 30px; top: 29px; width: 712px; height: 550px; }
  .front-photo {
    position: absolute; inset: 0;
    background: linear-gradient(180deg, var(--sunset-top) 0%, var(--sunset-bottom) 100%);
  }
  .front-panel {
    position: absolute; left: 162px; top: 0; width: 391px; height: 339px;
    background: var(--panel);
    text-align: center; color: var(--cream);
    font-family: "Oswald", sans-serif;
    text-shadow: 1px 1px 2px rgba(0,0,0,.5);
  }
  .brand { margin-top: 58px; font-weight: 700; font-size: 37px; line-height: 1; letter-spacing: .3px; text-transform: uppercase; }
  .guide-name { margin-top: 14px; font-weight: 600; font-size: 32px; line-height: 1; font-variant: small-caps; }
  .guide-role { margin-top: 10px; font-weight: 600; font-size: 25px; line-height: 1.1; letter-spacing: .5px; }
  .front-phone { margin-top: 46px; font-weight: 700; font-size: 44px; line-height: 1; }
  .front-web { margin-top: 14px; font-weight: 600; font-size: 25px; line-height: 1; text-transform: uppercase; letter-spacing: .5px; }
  .front-offer {
    position: absolute; left: 100px; top: 378px; width: 500px;
    font-family: "Sansita", sans-serif; font-weight: 700; color: var(--sage);
    text-shadow: 2px 2px 2px rgba(0,0,0,.6); text-align: center;
  }
  .offer-title { font-size: 40px; line-height: 1.1; }
  .offer-line { font-size: 30px; line-height: 1.5; }

  /* Back */
  .card--back { left: 35px; top: 613px; width: 713px; height: 554px; background: var(--back-bg); }
  .back-photo {
    position: absolute; left: 1px; top: 3px; width: 352px; height: 129px;
    background: linear-gradient(180deg, var(--photo-top) 0%, var(--photo-bottom) 100%);
  }
  .back-copy {
    position: absolute; left: 28px; top: 143px; width: 300px;
    font-family: "Arimo", sans-serif; font-size: 13.6px; line-height: 18.7px;
    color: var(--ink); letter-spacing: -.35px;
  }
  .back-copy .call-to-action { color: var(--teal); }
  .signoff {
    position: absolute; left: 93px; top: 424px;
    font-family: "Arimo", sans-serif; font-style: italic; font-weight: 700;
    font-size: 13.6px; line-height: 18.7px; color: var(--ink); letter-spacing: -.3px;
  }
  .contact { position: absolute; left: 93px; top: 461px; list-style: none; font-family: "Arimo", sans-serif; color: var(--teal); }
  .contact li { display: flex; align-items: center; gap: 8px; height: 20px; }
  .contact svg { width: 12px; height: 12px; flex: none; stroke: var(--ink); fill: none; stroke-width: 1.3; }
  .contact .phone { font-size: 13.6px; }
  .contact .small { font-size: 11.5px; text-transform: uppercase; letter-spacing: -.2px; }
  .stamp-box { position: absolute; left: 580px; top: 29px; width: 121px; height: 125px; border: 1.5px dashed var(--rule); }
  .address-line { position: absolute; left: 378px; width: 358px; border-top: 1.5px dashed var(--rule); }
  .address-line--1 { top: 279px; }
  .address-line--2 { top: 346px; }
  .address-line--3 { top: 413px; }
</style>
</head>
<body>

<section class="card card--front">
  <div class="front-photo" role="img" aria-label="Photo: sunset over a calm river with a fishing rod and lure in the foreground"></div>
  <div class="front-panel">
    <h1 class="brand">The Driftwood Caster</h1>
    <p class="guide-name">Wade Pellman</p>
    <p class="guide-role">Fishing Guide &amp; Outfitter</p>
    <p class="front-phone">1-800-555-0172</p>
    <p class="front-web">thedriftwoodcaster.test</p>
  </div>
  <div class="front-offer">
    <p class="offer-title">Smallmouth Bass</p>
    <p class="offer-line">One day guided fishing trips on</p>
    <p class="offer-line">the Kellow Creek Private Hollis</p>
  </div>
</section>

<section class="card card--back">
  <div class="back-photo" role="img" aria-label="Photo: panoramic view of a winding river through forested hills"></div>
  <p class="back-copy">
    The Kellow Creek's peaceful beauty is like no other river, the private Hollis section offers trophy bass fishing along with 100 fish days. Spin cast or fly fish for bass. This 8 hour fishing trip takes you into a remote section of ranches and wilderness abundant with not only thousands of bass per mile...... but wildlife and scenery are breathtaking in this quiet section of river. This trip is for everyone, easy for the Grand Parents and the grand kids...... Women love this trip with the warm weather and easy fishing. Vacation Rentals, Motels and R.V parks all available close by. <span class="call-to-action">So Let's go Fishing...... please call or email us today and book your trip or with any questions you have.</span>
  </p>
  <p class="signoff">Thank you for fishing with us!<br>Wade Pellman</p>
  <ul class="contact">
    <li class="phone"><svg viewBox="0 0 12 12"><circle cx="6" cy="6" r="5"/><path d="M4 3.5c0 2.5 2 4.5 4.5 4.5"/></svg>541-555-0148 or 800-555-0172</li>
    <li class="small"><svg viewBox="0 0 12 12"><rect x="1" y="2.5" width="10" height="7"/><path d="M1 2.5l5 4 5-4"/></svg>driftwoodcaster@mailbrook.test</li>
    <li class="small"><svg viewBox="0 0 12 12"><circle cx="6" cy="6" r="5"/><path d="M6 5v4M6 3v.8"/></svg>www.thedriftwoodcaster.test</li>
  </ul>
  <div class="stamp-box"></div>
  <div class="address-line address-line--1"></div>
  <div class="address-line address-line--2"></div>
  <div class="address-line address-line--3"></div>
</section>

</body>
</html>
```